Design some Business Cards for Halvern Co

Need professional modern sleek designed business cards for printing company.

logo supplied below

need in editable format, so contact details can be edited

```html
<!DOCTYPE html>
<html lang="en">
<head>
<meta charset="utf-8">
<title>Halvern Co — Business Cards</title>
<link href="https://fonts.googleapis.com/css2?family=Open+Sans:wght@400;600;700;800&display=swap" rel="stylesheet">
<style>
  :root {
    --page: #e9e6df;
    --card-dark: #3a3a3c;
    --card-light: #f7f7f7;
    --ink: #2c2c2e;
    --ink-soft: #4a4a4c;
    --accent-blue: #1aa3d9;
    --cyan: #19b3e6;
    --magenta: #d6288f;
    --yellow: #f2e21a;
    --black-tab: #2e2e30;
    --white: #ffffff;
  }
  * { margin: 0; padding: 0; box-sizing: border-box; }
  html, body {
    width: 1200px; height: 800px; overflow: hidden;
    background: var(--page);
    font-family: "Open Sans", Arial, sans-serif;
  }
  .sheet {
    width: 1200px; height: 800px;
    display: flex; align-items: center; justify-content: center; gap: 40px;
  }
  .card {
    position: relative;
    width: 540px; height: 310px;
    border-radius: 6px;
    overflow: hidden;
    box-shadow: 0 10px 24px rgba(0,0,0,0.18);
  }
  .card--front {
    background: var(--card-dark);
    display: flex; align-items: center; justify-content: center;
  }
  .card--back { background: var(--card-light); }

  .brand {
    display: flex; flex-direction: column; align-items: center; gap: 16px;
  }
  .brand__mark { width: 40px; height: 40px; background: var(--cyan); }
  .brand__name {
    font-weight: 800; font-size: 38px; letter-spacing: 0.5px; line-height: 1;
    text-transform: uppercase; white-space: nowrap;
  }
  .card--front .brand__name { color: var(--white); }
  .card--back .brand__name { color: var(--ink); font-size: 30px; }

  .card--back .brand {
    position: absolute; left: 36px; top: 96px; width: 230px;
  }

  .contact {
    position: absolute; left: 318px; top: 44px;
    color: var(--ink-soft); font-size: 13px; line-height: 1.35;
  }
  .contact__name { color: var(--accent-blue); font-weight: 700; font-size: 17px; line-height: 1.2; }
  .contact__role { font-size: 12px; margin-bottom: 22px; }
  .contact__address { margin-bottom: 6px; }
  .contact__list { list-style: none; }
  .contact__item { display: flex; align-items: center; gap: 8px; }
  .contact__icon { width: 11px; height: 11px; flex: none; }
  .contact__icon path, .contact__icon rect, .contact__icon circle { fill: none; stroke: var(--accent-blue); stroke-width: 1.6; }
  .contact__icon .solid { fill: var(--accent-blue); stroke: none; }

  .tabs {
    position: absolute; left: 0; right: 0; bottom: 0; height: 14px;
    display: flex; justify-content: space-between; padding: 0 22px;
  }
  .tab { width: 100px; height: 14px; border-radius: 6px 6px 0 0; }
  .tab--black { background: var(--black-tab); }
  .tab--cyan { background: var(--cyan); }
  .tab--yellow { background: var(--yellow); }
  .tab--magenta { background: var(--magenta); }
</style>
</head>
<body>
  <main class="sheet">
    <section class="card card--front" aria-label="Card front">
      <div class="brand">
        <span class="brand__mark"></span>
        <span class="brand__name">Halvern Co</span>
      </div>
    </section>

    <section class="card card--back" aria-label="Card back">
      <div class="brand">
        <span class="brand__mark"></span>
        <span class="brand__name">Halvern Co</span>
      </div>

      <div class="contact">
        <p class="contact__name">John Doe</p>
        <p class="contact__role">Manager</p>
        <p class="contact__address">POX BOX 123 city,<br>123 country</p>
        <ul class="contact__list">
          <li class="contact__item">
            <svg class="contact__icon" viewBox="0 0 12 12"><path class="solid" d="M2.5 1 L4.5 1 L5.2 3.6 L3.9 4.6 Q5 7 7.4 8.1 L8.4 6.8 L11 7.5 L11 9.5 Q10.5 11 8.8 11 Q1 10 1 2.8 Q1 1.2 2.5 1 Z"/></svg>
            <span>111-222-333</span>
          </li>
          <li class="contact__item">
            <svg class="contact__icon" viewBox="0 0 12 12"><rect x="3" y="1" width="6" height="10" rx="1"/></svg>
            <span>111-222-333</span>
          </li>
          <li class="contact__item">
            <svg class="contact__icon" viewBox="0 0 12 12"><rect x="1" y="2.5" width="10" height="7"/><path d="M1 2.5 L6 6.5 L11 2.5"/></svg>
            <span>info@youremail.com</span>
          </li>
          <li class="contact__item">
            <svg class="contact__icon" viewBox="0 0 12 12"><circle cx="6" cy="6" r="4.8"/><path d="M1.2 6 H10.8 M6 1.2 Q3.5 6 6 10.8 M6 1.2 Q8.5 6 6 10.8"/></svg>
            <span>www.yourwebsite.com</span>
          </li>
        </ul>
      </div>

      <div class="tabs">
        <span class="tab tab--black"></span>
        <span class="tab tab--cyan"></span>
        <span class="tab tab--yellow"></span>
        <span class="tab tab--magenta"></span>
      </div>
    </section>
  </main>
</body>
</html>
```